website conversion to Wordpress with an updated look and feel

Brim Tarn Works Limited is a company and an online presence, which promotes and sells a branded fuel additive product named “Pelvix”.

The existing website is at www.brimtarnworks.co.uk

The site consists of static but attractive pages, a contact form, and most importantly a shopping page which is driven externally using shopvarn.com. Therefore e-commerce coding is NOT required as this task is performed by shopvarn via a plugin.

The website is 4 years old and we intend to revamp the graphics and the image of the company and the website to give it a modern “Windows 10” look!

Less text and less cluttering, Cleaner and easier navigations, bigger and clearer fonts. Simple message to put across to visitors/potential customers. Be creative.

The site needs to be simplified - the detail can/should still be there... But it can be placed deeper down or hidden by the use of dropdowns, callouts, etc.

A couple of good example styles we like are

https://www.gullmoth.com/
http://www.9brassling.com/en/#/welcome
https://www.slatetorro.com/

Some specific areas of attention.

homepage - This needs to really reflect the new look-and feel of the website. In addition the product we sell can be used in a number of applications - currently navigation to these different applications is through the moving banner. This needs to be changed. The major areas for access should be

Heating Oil
Vehicles
Marine
Generators

Technical requirements what we want:-
Wordpress (self hosted ) - currently Joomla based
Use of webfonts to improve typographic appearances
Shopvarn integration using plugin
Facebook/Twitter integration
Responsive design (Mobile friendly)
Search Engine friendly and some SEO optimisation
Google Analytics / Bing webmaster tracking

Target Market(s)

Owners of Tolv branded range cookers and similar - our product fixes a fuel problem specific to these devices.

Also bulk fuel users looking to save money on their fuel costs - product improves fuel efficiency and reduces maintenance.

Industry/Entity Type

E-Commerce

Font styles to use
Sans Serif

Requirements
Must have
• Wordpress design
• Responsive design
• Simple "clean" look and feel
• Use of stock graphics
• a review of all current pages
Nice to have
• Social media integration - blog
• A forum to discuss the product and problems people experience with fuel

```html
<!DOCTYPE html>
<html lang="en">
<head>
<meta charset="utf-8">
<title>Brim Tarn Works Limited — Applications</title>
<link rel="stylesheet" href="https://fonts.googleapis.com/css2?family=Open+Sans:wght@300;400&display=swap">
<style>
  :root {
    --green: #65a133;
    --green-band: #68a535;
    --tile-grey: #dedede;
    --ink: #111111;
    --top-dark: #3c3c3c;
    --white: #ffffff;
    --mist: #e9ebec;
  }
  * { margin: 0; padding: 0; box-sizing: border-box; }
  html, body {
    width: 1200px;
    height: 602px;
    overflow: hidden;
  }
  body {
    position: relative;
    font-family: "Open Sans", Arial, sans-serif;
    background:
      radial-gradient(ellipse 700px 140px at 600px 60px, var(--white) 0%, rgba(255,255,255,0) 70%),
      radial-gradient(ellipse 1300px 220px at 600px 90px, var(--mist) 0%, rgba(233,235,236,0) 75%),
      linear-gradient(180deg, #f1f2f3 0%, var(--white) 35%, var(--white) 70%, #f4f9fa 100%);
  }
  .top-bar {
    position: absolute;
    left: 0; top: 0;
    width: 1200px; height: 17px;
    background: linear-gradient(180deg, #555 0%, var(--top-dark) 100%);
  }
  .top-band {
    position: absolute;
    left: 0; top: 17px;
    width: 1200px; height: 13px;
    background: var(--green-band);
  }
  .bottom-band {
    position: absolute;
    left: 0; top: 584px;
    width: 1200px; height: 18px;
    background: var(--green-band);
  }
  .applications {
    position: absolute;
    left: 139px; top: 175px;
    display: flex;
    gap: 20px;
  }
  .application-tile {
    position: relative;
    width: 221px;
    height: 331px;
    background: var(--tile-grey);
    color: var(--ink);
    text-decoration: none;
    display: block;
  }
  .application-tile.is-active { background: var(--green); }
  .application-icon {
    position: absolute;
    left: 0; top: 50px;
    width: 221px; height: 160px;
  }
  .application-label {
    position: absolute;
    left: 0; right: 0; top: 260px;
    text-align: center;
    font-weight: 300;
    font-size: 29px;
    letter-spacing: 0.2px;
    white-space: nowrap;
  }
</style>
</head>
<body>
  <div class="top-bar"></div>
  <div class="top-band"></div>

  <nav class="applications" aria-label="Applications">
    <a class="application-tile is-active" href="#heating-oil">
      <svg class="application-icon" viewBox="0 0 221 160" aria-hidden="true">
        <path fill="#fff" d="M23 11 L40 5 L58 17 L62 14 L163 14 L181 30 L181 157 L53 157 L53 52 L45 44 L41 24 L30 24 Z"/>
        <rect x="104" y="28" width="28" height="8" fill="var(--green)"/>
        <g fill="none" stroke="var(--green)" stroke-width="9">
          <rect x="89" y="67" width="43" height="43"/>
          <path d="M80 58 L95 73 M141 58 L126 73 M80 119 L95 104 M141 119 L126 104" stroke-width="8"/>
        </g>
      </svg>
      <span class="application-label">HEATING OIL</span>
    </a>

    <a class="application-tile" href="#vehicles">
      <svg class="application-icon" viewBox="0 0 221 160" aria-hidden="true">
        <g fill="#000">
          <path d="M95 20 Q100 10 112 10 L150 10 Q162 10 166 20 L172 36 Q176 38 176 46 L176 80 L166 80 L166 90 L150 90 L150 70 L108 70 L92 36 Z"/>
          <path d="M48 40 Q52 30 64 30 L104 30 Q116 30 120 40 L127 56 Q132 58 132 66 L132 98 L122 98 L122 110 L106 110 L106 100 L62 100 L62 110 L46 110 L46 98 L36 98 L36 66 Q36 58 41 56 Z"/>
          <path d="M86 74 Q90 64 102 64 L146 64 Q158 64 162 74 L170 92 Q175 94 175 102 L175 134 L165 134 L165 146 L149 146 L149 136 L99 136 L99 146 L83 146 L83 134 L73 134 L73 102 Q73 94 78 92 Z"/>
        </g>
        <g fill="var(--tile-grey)">
          <path d="M57 42 L111 42 L117 58 L51 58 Z"/>
          <path d="M96 76 L152 76 L159 93 L89 93 Z"/>
          <circle cx="90" cy="110" r="5"/><circle cx="158" cy="110" r="5"/>
          <rect x="108" y="116" width="32" height="6"/>
        </g>
        <path d="M76 96 L82 92 L82 104 Z M171 96 L165 92 L165 104 Z" fill="#000"/>
      </svg>
      <span class="application-label">VEHICLES</span>
    </a>

    <a class="application-tile" href="#marine">
      <svg class="application-icon" viewBox="0 0 221 160" aria-hidden="true">
        <g fill="#000">
          <path d="M83 48 L83 28 Q83 16 95 16 L104 16 L104 28 L95 28 L95 48 Z"/>
          <ellipse cx="111" cy="89" rx="63" ry="40"/>
          <rect x="170" y="82" width="14" height="14"/>
          <rect x="176" y="70" width="8" height="38" rx="3"/>
        </g>
        <g fill="var(--tile-grey)">
          <circle cx="86" cy="89" r="10"/>
          <circle cx="112" cy="89" r="10"/>
          <circle cx="138" cy="89" r="10"/>
        </g>
      </svg>
      <span class="application-label">MARINE</span>
    </a>

    <a class="application-tile" href="#generators">
      <svg class="application-icon" viewBox="0 0 221 160" aria-hidden="true">
        <g fill="#000">
          <rect x="95" y="26" width="62" height="50"/>
          <rect x="55" y="50" width="115" height="85"/>
          <rect x="45" y="70" width="10" height="40"/>
          <rect x="170" y="70" width="10" height="40"/>
          <rect x="68" y="130" width="16" height="13" rx="2"/>
          <rect x="142" y="130" width="16" height="13" rx="2"/>
        </g>
        <g fill="var(--tile-grey)">
          <path d="M100 52 L152 52 L152 68 Q152 76 144 76 L100 76 Z" fill="none"/>
          <path d="M92 76 L160 76 L160 80 L92 80 Z"/>
          <path d="M130 34 L118 54 L126 54 L120 70 L136 48 L128 48 L134 34 Z"/>
          <rect x="66" y="60" width="16" height="3"/><rect x="66" y="67" width="16" height="3"/>
          <rect x="66" y="74" width="16" height="3"/><rect x="66" y="96" width="16" height="3"/>
          <rect x="66" y="103" width="16" height="3"/><rect x="66" y="110" width="16" height="3"/>
          <rect x="66" y="117" width="16" height="3"/>
        </g>
        <rect x="95" y="26" width="62" height="50" fill="none" stroke="#000" stroke-width="2"/>
      </svg>
      <span class="application-label">GERARATORS</span>
    </a>
  </nav>

  <div class="bottom-band"></div>
</body>
</html>
```